Travel Agency Website - Simple General

Need a 7 page simple design that is pretty repetitive. Need to be able to load quickly that is SEO optimized. Trying to give ideas on what they can do, be personal as we are local, but at the same time come across as professional and get information easily with little burden.

- Landing Page
- Marrowind Vacations Page
- Family Trips
- Road Trips from Texas
- Other Destinations
- About Us Page
- Contact Us Page

Target Market(s)

Families

Coding

Coded - Design and coding required

Number of Pages Required

5+ page

Colors

Designer to choose colors to be used in the design.

Requirements
Must have
• Like it to flow easily with our logo. Use that for colors, etc.

```html
<!DOCTYPE html>
<html lang="en">
<head>
<meta charset="utf-8">
<title>Wayfare &amp; Wonder Travel Co.</title>
<link href="https://fonts.googleapis.com/css2?family=Allura&family=Figtree:wght@400;500&display=swap" rel="stylesheet">
<style>
:root{
  --cream:#fdf8ef;
  --teal-dark:#2e6670;
  --teal:#4b9ea8;
  --teal-light:#8cbcbf;
  --gold:#c9a266;
  --text:#3a3a3a;
  --white:#ffffff;
}
*{box-sizing:border-box;margin:0;padding:0}
html,body{width:1200px;height:2932px;overflow:hidden}
body{background:var(--cream);font-family:"Figtree",sans-serif;color:var(--text);position:relative}
.abs{position:absolute}
.script{font-family:"Allura",cursive;color:var(--teal-dark);font-weight:400}

.nav{left:46px;top:55px;width:1104px;height:67px;border-radius:34px;border:1.5px solid var(--gold);
  background:linear-gradient(180deg,var(--teal),var(--teal-light));}
.nav a{position:absolute;top:24px;color:var(--white);font-size:14px;text-decoration:none;white-space:nowrap}
.brand-badge{left:531px;top:32px;width:134px;height:112px;border-radius:26px;background:var(--cream);
  border:2px solid var(--teal-light);display:flex;flex-direction:column;align-items:center;justify-content:center;text-align:center}
.brand-badge span{font-family:"Figtree",sans-serif;font-weight:500;color:var(--teal-dark);font-size:15px;line-height:1.2}

.heading{width:100%;text-align:center;left:0;white-space:nowrap}
.btn{display:flex;align-items:center;justify-content:center;border-radius:26px;font-family:"Allura",cursive;font-size:21px;text-decoration:none;white-space:nowrap}
.btn-fill{background:linear-gradient(180deg,var(--teal),var(--teal-light));color:var(--white);border:1.5px solid var(--gold)}
.btn-line{background:var(--cream);color:var(--teal-dark);border:1.5px solid var(--gold)}

.hero-art{left:43px;top:427px;width:1114px;height:563px;border-radius:48% 48% 30% 30% / 40% 40% 20% 20%;
  background:radial-gradient(ellipse at 50% 55%,#e8c9c4 0%,#c9d9e6 45%,#e4ecf1 70%,var(--cream) 100%)}

.card{top:1201px;width:308px;height:281px;background:var(--white);border:1.5px solid #e7d3ad;border-radius:22px;padding:30px 22px 0 23px}
.card h3{font-size:30px;margin-bottom:10px;white-space:nowrap}
.card p{font-size:15px;line-height:26px}
.card .btn{position:absolute;left:22px;top:201px;height:50px}
.arrow{top:1328px}

.para{left:140px;width:920px;text-align:center;font-size:15px;line-height:26px}

.photo{left:113px;top:2073px;width:413px;height:352px;border-radius:20px;
  background:linear-gradient(135deg,#dfe6e3,#c7b7ae 45%,#e9a0a8 75%,#f0c64c)}
.plan h2{font-size:46px;line-height:56px;margin-bottom:18px;white-space:nowrap}
.plan p{font-size:15px;line-height:26px}

.footer{left:46px;top:2506px;width:1105px;height:386px;border-radius:28px;border:1.5px solid var(--gold);
  background:linear-gradient(180deg,var(--teal),var(--teal-light));color:var(--white)}
.footer .script{color:var(--white)}
.footer .about p{font-size:16px;line-height:34px;text-transform:uppercase}
.footer .rule{left:0;top:332px;width:100%;height:1px;background:rgba(255,255,255,.6)}
.contact-row{display:flex;align-items:center;gap:12px;font-size:16px;margin-top:14px}
.icon{width:34px;height:34px;border-radius:50%;background:var(--white);display:flex;align-items:center;justify-content:center}
</style>
</head>
<body>

<header class="abs nav">
  <a style="left:56px" href="#">HOME</a>
  <a style="left:116px" href="#">MARROWIND VACATIONS</a>
  <a style="left:305px" href="#">OTHER DESTINATIONS</a>
  <a style="left:635px" href="#">TEXAS ROAD TRIPS</a>
  <a style="left:794px" href="#">FAMILY TRIPS</a>
  <a style="left:916px" href="#">ABOUT</a>
  <a style="left:993px" href="#">CONTACT</a>
</header>
<div class="abs brand-badge"><span>Wayfare &amp;<br>Wonder<br>Travel Co.</span></div>

<h1 class="abs heading script" style="top:238px;font-size:50px">Adventure Begins With a Whistle</h1>
<a class="abs btn btn-fill" style="left:390px;top:344px;width:196px;height:50px" href="#">Start Your Journey</a>
<a class="abs btn btn-line" style="left:605px;top:344px;width:199px;height:50px" href="#">Explore Destinations</a>

<div class="abs hero-art" role="img" aria-label="Watercolor illustration of a fairytale castle among soft clouds and trees"></div>

<h2 class="abs heading script" style="top:1088px;font-size:50px">Explore Your Next Adventure</h2>

<svg class="abs arrow" style="left:50px" width="30" height="26" viewBox="0 0 30 26" fill="none" stroke="#4b9ea8" stroke-width="2.5" stroke-linecap="round" stroke-linejoin="round"><path d="M28 13H3M12 3L2 13l10 10"/></svg>
<svg class="abs arrow" style="left:1119px" width="30" height="26" viewBox="0 0 30 26" fill="none" stroke="#4b9ea8" stroke-width="2.5" stroke-linecap="round" stroke-linejoin="round"><path d="M2 13h25M18 3l10 10-10 10"/></svg>

<article class="abs card" style="left:112px">
  <h3 class="script">Marrowind Vacations</h3>
  <p>From magical Marrowind parks to unforgettable Marrowind cruises, we help create stress-free vacations full of wonder.</p>
  <a class="btn btn-fill" style="width:196px" href="#">Start Your Journey</a>
</article>
<article class="abs card" style="left:447px">
  <h3 class="script">Family Trips</h3>
  <p>Browse family-tested adventures and curated travel experiences designed to bring everyone together.</p>
  <a class="btn btn-fill" style="width:228px" href="#">View Family Adventures</a>
</article>
<article class="abs card" style="left:782px">
  <h3 class="script">Texas Road Trips</h3>
  <p>Hit the road with custom Texas itineraries and optional van rentals through Pineway Van Rentals.</p>
  <a class="btn btn-fill" style="width:196px" href="#">Plan a Road Trip</a>
</article>

<h2 class="abs heading script" style="top:1612px;font-size:54px">Meet the Family Behind Wayfare &amp; Wonder</h2>
<p class="abs para" style="top:1706px">At Wayfare &amp; Wonder, we believe travel is about more than reaching a destination — it’s about creating unforgettable memories along the way. From magical Marrowind vacations to scenic road trips and relaxing family getaways, we’re passionate about helping families and travelers experience stress-free adventures tailored just for them.</p>
<p class="abs para" style="top:1809px">What started as a love for exploring together quickly became a passion for helping others discover the joy of travel. We understand how important it is to create vacations that feel exciting, seamless, and meaningful, which is why every trip we plan is personalized to fit your travel style, budget, and dreams.</p>
<a class="abs btn btn-fill" style="left:500px;top:1918px;width:194px;height:50px" href="#">Start Your Journey</a>

<div class="abs photo" role="img" aria-label="Photo of a family planning a trip together on a laptop beside a packed suitcase"></div>
<section class="abs plan" style="left:599px;top:2100px;width:490px">
  <h2 class="script">Let’s Plan Your Next Adventure</h2>
  <p style="margin-bottom:22px">Whether you’re dreaming of a magical Marrowind vacation, a scenic Texas road trip, or a relaxing family getaway, we’re here to help make the planning process simple and stress-free.</p>
  <p>Fill out the form below and tell us a little about your travel plans — we can’t wait to help create your perfect vacation.</p>
</section>
<a class="abs btn btn-fill" style="left:598px;top:2360px;width:194px;height:50px" href="#">Start Your Journey</a>

<footer class="abs footer">
  <div class="abs about" style="left:69px;top:48px">
    <h4 class="script" style="font-size:32px;margin-bottom:10px">About</h4>
    <p>Creating magical vacations,<br>unforgettable family adventures,<br>and stress-free travel experiences<br>designed just for you.</p>
  </div>
  <div class="abs brand-badge" style="left:440px;top:62px;width:222px;height:176px;border-radius:40px">
    <span style="font-size:24px">Wayfare &amp;<br>Wonder<br>Travel Co.</span>
  </div>
  <div class="abs" style="left:741px;top:78px">
    <h4 class="script" style="font-size:32px">Contact Us</h4>
    <div class="contact-row">
      <span class="icon"><svg width="18" height="18" viewBox="0 0 24 24" fill="#4b9ea8"><path d="M6.6 10.8a15.1 15.1 0 006.6 6.6l2.2-2.2a1 1 0 011-.25 11.4 11.4 0 003.6.57 1 1 0 011 1V20a1 1 0 01-1 1A17 17 0 013 4a1 1 0 011-1h3.5a1 1 0 011 1c0 1.25.2 2.45.57 3.6a1 1 0 01-.25 1z"/></svg></span>
      555.014.2290
    </div>
    <div class="contact-row">
      <span class="icon"><svg width="18" height="14" viewBox="0 0 24 18" fill="none" stroke="#4b9ea8" stroke-width="2"><rect x="1" y="1" width="22" height="16" rx="2"/><path d="M1 2l11 8 11-8"/></svg></span>
      hello@wayfarewonder.example
    </div>
  </div>
  <div class="abs rule"></div>
  <p class="abs" style="left:0;top:346px;width:100%;text-align:center;font-size:13px">© 2026 Wayfare &amp; Wonder Travel Co. All Rights Reserved.</p>
</footer>

</body>
</html>
```